vireLattice "organisation chart"

We need a new Organisation Chart for our Company! We are actually in a Change-management-process and will Change from a hierarchical Organisation in to a Network Organisation. Therefor we need a new Organisation Chart.
The following departements must be visible and legible on the Chart:
Team Sales & Consulting
Team Productmanagement
Team Supply Chain
Team Human Resources
Team Smart Digital Development
Team Marketing & Communication
The title of the Chart ist «vireLattice»
The Colors of the back of the Chart must be: RGB 73/25/102 // Pantone 2627
The Colors for the different Teams should be:
Team Sales & Consulting (Pantone: 803/neon yellow = Background)
Team Productmanagement (Pantone: 804/neon orange = Background)
Team Supply Chain (Pantone: 802/neon green = Background)
Team Human Resources (Pantone: 801/neon blue = Background)
Team Smart Digital Development (Pantone: 805/neon red = Background)
Team Marketing & Communication (Pantone: 803/neon pink = Background)
See below (upload files) an example showing a self-made Chart ... :-)
Our font is: Univers LT Std // Please feel free to Combine the Fonts Colors with the background colors
It Company

```html
<!DOCTYPE html>
<html lang="en">
<head>
<meta charset="utf-8">
<title>vireLattice – Organisation Chart</title>
<link rel="stylesheet" href="https://fonts.googleapis.com/css2?family=Archivo:wght@700&family=Nunito:wght@800;900&display=swap">
<style>
  :root {
    --frame: #a38bbd;
    --board: #5a3589;
    --title-bg: #f5aad0;
    --title-ink: #1d1a1b;
    --link: #f4a9cf;
    --shadow: #231f20;
    --team-ink: #ffffff;
    --sales: #f6df1f;
    --product: #fba93f;
    --supply: #4db748;
    --hr: #00aeda;
    --digital: #f26c67;
    --marketing: #e53f7e;
  }
  html, body {
    margin: 0;
    padding: 0;
    width: 1200px;
    height: 1200px;
    overflow: hidden;
    background: var(--frame);
  }
  .org-chart { display: block; width: 1200px; height: 1200px; }
  .frame { fill: var(--frame); }
  .board { fill: var(--board); }
  .title-plate { fill: var(--title-bg); }
  .title-text {
    font-family: "Archivo", "Helvetica Neue", Arial, sans-serif;
    font-weight: 700;
    font-size: 50px;
    fill: var(--title-ink);
  }
  .link {
    stroke: var(--link);
    stroke-width: 7;
    fill: none;
  }
  .arrow-head { fill: var(--link); }
  .team-shadow { fill: var(--shadow); }
  .team-label {
    font-family: "Nunito", "Arial Rounded MT Bold", Arial, sans-serif;
    font-weight: 900;
    font-size: 27px;
    fill: var(--team-ink);
  }
  .team-label--compact { font-size: 24px; }
  .team--sales .team-shape { fill: var(--sales); }
  .team--product .team-shape { fill: var(--product); }
  .team--supply .team-shape { fill: var(--supply); }
  .team--hr .team-shape { fill: var(--hr); }
  .team--digital .team-shape { fill: var(--digital); }
  .team--marketing .team-shape { fill: var(--marketing); }
</style>
</head>
<body>
<svg class="org-chart" viewBox="0 0 1000 1000" xmlns="http://www.w3.org/2000/svg" role="img" aria-label="vireLattice network organisation chart">
  <defs>
    <marker id="arrowHead" viewBox="0 0 10 10" refX="7" refY="5" markerWidth="4" markerHeight="4" orient="auto-start-reverse">
      <path class="arrow-head" d="M0,0 L10,5 L0,10 Z"/>
    </marker>
    <polygon id="hexagon" points="-122,0 -61,-105 61,-105 122,0 61,105 -61,105"/>
  </defs>

  <rect class="frame" x="0" y="0" width="1000" height="1000"/>
  <rect class="board" x="40" y="65" width="920" height="893" rx="50"/>

  <g class="title">
    <rect class="title-plate" x="297" y="30" width="406" height="70"/>
    <text class="title-text" x="500" y="82" text-anchor="middle">vireLattice</text>
  </g>

  <g class="links">
    <line class="link" x1="466" y1="247" x2="536" y2="247" marker-start="url(#arrowHead)" marker-end="url(#arrowHead)"/>
    <line class="link" x1="727" y1="358" x2="763" y2="418" marker-start="url(#arrowHead)" marker-end="url(#arrowHead)"/>
    <line class="link" x1="763" y1="640" x2="727" y2="700" marker-start="url(#arrowHead)" marker-end="url(#arrowHead)"/>
    <line class="link" x1="536" y1="812" x2="466" y2="812" marker-start="url(#arrowHead)" marker-end="url(#arrowHead)"/>
    <line class="link" x1="273" y1="700" x2="237" y2="640" marker-start="url(#arrowHead)" marker-end="url(#arrowHead)"/>
    <line class="link" x1="237" y1="418" x2="273" y2="358" marker-start="url(#arrowHead)" marker-end="url(#arrowHead)"/>
    <line class="link" x1="322" y1="527" x2="676" y2="527" marker-start="url(#arrowHead)" marker-end="url(#arrowHead)"/>
    <line class="link" x1="412" y1="378" x2="584" y2="676" marker-start="url(#arrowHead)" marker-end="url(#arrowHead)"/>
    <line class="link" x1="584" y1="378" x2="412" y2="676" marker-start="url(#arrowHead)" marker-end="url(#arrowHead)"/>
  </g>

  <g class="team team--sales" transform="translate(337 247)">
    <use href="#hexagon" class="team-shadow" x="5" y="5"/>
    <use href="#hexagon" class="team-shape"/>
    <text class="team-label" text-anchor="middle">
      <tspan x="0" y="-30">Team</tspan>
      <tspan x="0" y="1">Sales &amp;</tspan>
      <tspan x="0" y="32">Consulting</tspan>
    </text>
  </g>

  <g class="team team--product" transform="translate(663 247)">
    <use href="#hexagon" class="team-shadow" x="5" y="5"/>
    <use href="#hexagon" class="team-shape"/>
    <text class="team-label team-label--compact" text-anchor="middle">
      <tspan x="0" y="-30">Team</tspan>
      <tspan x="0" y="0">Product</tspan>
      <tspan x="0" y="30">management</tspan>
    </text>
  </g>

  <g class="team team--supply" transform="translate(827 530)">
    <use href="#hexagon" class="team-shadow" x="5" y="5"/>
    <use href="#hexagon" class="team-shape"/>
    <text class="team-label" text-anchor="middle">
      <tspan x="0" y="-28">Team</tspan>
      <tspan x="0" y="3">Supply</tspan>
      <tspan x="0" y="34">Chain</tspan>
    </text>
  </g>

  <g class="team team--hr" transform="translate(663 812)">
    <use href="#hexagon" class="team-shadow" x="5" y="5"/>
    <use href="#hexagon" class="team-shape"/>
    <text class="team-label" text-anchor="middle">
      <tspan x="0" y="-24">Team</tspan>
      <tspan x="0" y="7">Human</tspan>
      <tspan x="0" y="38">Resources</tspan>
    </text>
  </g>

  <g class="team team--digital" transform="translate(337 812)">
    <use href="#hexagon" class="team-shadow" x="5" y="5"/>
    <use href="#hexagon" class="team-shape"/>
    <text class="team-label team-label--compact" text-anchor="middle">
      <tspan x="0" y="-31">Team</tspan>
      <tspan x="0" y="0">Smart Digital</tspan>
      <tspan x="0" y="31">Development</tspan>
    </text>
  </g>

  <g class="team team--marketing" transform="translate(172 530)">
    <use href="#hexagon" class="team-shadow" x="5" y="5"/>
    <use href="#hexagon" class="team-shape"/>
    <text class="team-label team-label--compact" text-anchor="middle">
      <tspan x="0" y="-29">Team</tspan>
      <tspan x="0" y="2">Marketing &amp;</tspan>
      <tspan x="0" y="33">Communication</tspan>
    </text>
  </g>
</svg>
</body>
</html>
```